Boutique Financial Services/Advisor Business Needs Web Design

Looking for an informational and functional web design for my Financial Services/Financial Advisement business. It should have functionality for Company name, address, phone #, "About Us", Who we are, Our Mission, Services we offer, Biographies/Photos of/about "The Team", and possibly a link to "Contact Us". Would like to see something new & exciting blended with a traditional/professional look that will appeal to those approaching retirement, as well as those younger clients that are beginning to think about planning for the future. I already have a web domain through Brixwell, but would like this to be the design we use for that domain.
Financial Services/Financial Advisor
Coded - Design and coding required
1 page

```html
<!DOCTYPE html>
<html lang="en">
<head>
<meta charset="utf-8">
<title>Alderpeak Wealth Management</title>
<link href="https://fonts.googleapis.com/css2?family=Cinzel:wght@400;700&family=Poppins:wght@400;500;600;700&display=swap" rel="stylesheet">
<style>
:root{
  --navy:#0c0b4f;
  --grey:#9e9e9e;
  --grey-light:#f6f6f6;
  --diamond-grey:#a9a9a9;
  --text:#444;
  --white:#fff;
}
*{margin:0;padding:0;box-sizing:border-box}
html,body{width:1200px;height:4458px;overflow:hidden}
body{position:relative;background:var(--white);font-family:'Poppins',sans-serif;color:var(--text)}
.abs{position:absolute}

/* header */
.topbar{left:0;top:0;width:1200px;height:43px;background:var(--navy);color:var(--white);font-size:13px;z-index:3}
.topbar .phone{left:68px;top:13px;display:flex;align-items:center;gap:10px}
.topbar .mail{right:64px;top:12px;display:flex;align-items:center;gap:10px}
.navbar{left:0;top:43px;width:1200px;height:52px;background:var(--white);box-shadow:0 2px 6px rgba(0,0,0,.06);z-index:3}
.nav-link{top:62px;font-size:12px;color:#222;letter-spacing:.2px;z-index:4}
.nav-link.active{color:var(--navy);font-weight:500}
.logo-plate{left:0;top:0;width:1200px;height:160px;z-index:5;pointer-events:none}
.brand{left:450px;top:72px;width:317px;text-align:center;color:var(--navy);font-family:'Cinzel',serif;font-weight:400;line-height:1.1;z-index:6}
.brand .l1{font-size:22px;display:block}
.brand .l2{font-size:17px;display:block;letter-spacing:1px}
.brand-dot{left:593px;top:22px;width:30px;height:30px;border-radius:50%;background:var(--navy);z-index:6}

/* hero */
.hero-photo{left:0;top:95px;width:1200px;height:735px;z-index:1;
  background:radial-gradient(ellipse 520px 380px at 120px 640px,#6d7a3e 0%,rgba(109,122,62,0) 100%),
             linear-gradient(180deg,#d9e0e7 0%,#c5cfda 50%,#93a2b2 100%);
  clip-path:polygon(0 0,1200px 0,1200px 563px,599px 705px,0 570px)}
.hero-edge{left:0;top:640px;width:1200px;height:200px;z-index:2}
.hero-kicker{left:607px;top:290px;width:400px;text-align:center;font-weight:700;font-size:34px;color:var(--navy);letter-spacing:.5px;z-index:2}
.hero-title{left:430px;top:340px;width:755px;text-align:center;font-family:'Cinzel',serif;font-size:66px;line-height:82px;color:var(--navy);z-index:2}
.btn{display:flex;align-items:center;justify-content:center;gap:14px;border-radius:40px;font-weight:500}
.btn-hero{left:679px;top:528px;width:254px;height:62px;background:var(--navy);color:var(--white);font-size:19px;box-shadow:0 0 0 3px #fff inset, 0 0 0 1px var(--navy);z-index:2}
.scroll-cue{left:577px;top:800px;width:44px;height:44px;border-radius:50%;background:var(--white);border:2px solid #b5b5b5;display:flex;align-items:center;justify-content:center;z-index:3}

/* about */
.about-photo{left:160px;top:935px;width:384px;height:384px;border-radius:50%;
  background:radial-gradient(circle at 50% 40%,#d9d9d9 0%,#a7a7a7 55%,#3b3e45 100%);
  border:8px solid #fff;box-shadow:0 6px 22px rgba(0,0,0,.18)}
.about-title{left:630px;top:925px;font-family:'Cinzel',serif;font-size:46px;color:var(--navy)}
.about-sub{left:631px;top:982px;font-size:14px;color:#333;display:flex;align-items:center;gap:12px}
.rule{display:inline-block;height:3px;background:var(--navy)}
.about-text{left:630px;top:1033px;width:425px;font-size:13.4px;line-height:26.6px;text-align:justify;color:var(--text)}
.btn-small{left:630px;top:1276px;width:186px;height:44px;background:var(--navy);color:var(--white);font-size:13.5px}

/* why */
.why-bg{left:0;top:1411px;width:1200px;height:861px}
.why-kicker{left:0;top:1554px;width:1200px;text-align:center;font-size:15px;color:#333;display:flex;justify-content:center;align-items:center;gap:12px}
.why-title{left:0;top:1585px;width:1200px;text-align:center;font-family:'Cinzel',serif;font-size:47px;line-height:57px;color:var(--navy)}
.emblem-mark{left:490px;top:1870px;width:220px;height:220px;border-radius:50%;background:var(--navy)}
.emblem-name{left:400px;top:2120px;width:400px;text-align:center;font-family:'Cinzel',serif;font-size:30px;line-height:38px;color:var(--navy)}
.feat-diamond{width:98px;height:98px;transform:rotate(45deg);box-shadow:0 4px 10px rgba(0,0,0,.12)}
.feat-diamond.navy{background:var(--navy)}
.feat-diamond.light{background:var(--diamond-grey)}
.feat-icon{width:60px;height:60px}
.feat-title{font-family:'Cinzel',serif;font-weight:700;font-size:16px;line-height:18px;color:var(--navy);text-transform:uppercase}
.feat-text{font-size:13px;line-height:20px;color:var(--text);margin-top:6px}
.feat.right{text-align:right}

/* services */
.services{left:0;top:2272px;width:1200px;height:1102px;background:var(--grey)}
.svc-title{left:0;top:2410px;width:1200px;text-align:center;font-family:'Cinzel',serif;font-size:48px;color:var(--white)}
.svc-sub{left:0;top:2469px;width:1200px;font-size:14px;color:var(--white);display:flex;justify-content:center;align-items:center;gap:8px}
.svc-sub .rule{background:var(--white);height:2px}
.svc-intro{left:150px;top:2533px;width:900px;text-align:center;font-size:13.5px;line-height:27px;color:var(--white)}
.svc-diamond{width:240px;height:240px;background:var(--white);transform:rotate(45deg);box-shadow:0 0 28px rgba(255,255,255,.9)}
.svc-diamond.featured{background:var(--navy);box-shadow:0 0 18px rgba(12,11,79,.4)}
.svc-icon{width:68px;height:68px;border-radius:50%;background:var(--navy);border:3px solid #fff;box-shadow:0 0 0 2px var(--navy);display:flex;align-items:center;justify-content:center}
.svc-icon.invert{background:var(--white);box-shadow:0 0 0 2px var(--white)}
.svc-label{width:260px;text-align:center;font-weight:600;font-size:18px;color:#222}
.svc-label.light{color:var(--white)}
.pill-read{left:561px;top:2859px;width:88px;height:22px;border-radius:12px;background:var(--white);color:var(--navy);font-size:9px;font-weight:600;display:flex;align-items:center;justify-content:center}
.btn-view{left:513px;top:3178px;width:185px;height:47px;background:var(--navy);color:var(--white);font-size:14px;box-shadow:0 0 0 2px #fff}

/* cta */
.cta{left:0;top:3374px;width:1200px;height:1025px;background:var(--navy)}
.cta-kicker{left:0;top:3483px;width:1200px;text-align:center;color:var(--white);font-size:15px}
.cta-title{left:0;top:3512px;width:1200px;text-align:center;color:var(--white);font-family:'Cinzel',serif;font-size:50px;line-height:57px}
.cta-last{left:0;top:3632px;width:1200px;display:flex;justify-content:center;align-items:center;gap:22px;color:var(--white);font-family:'Cinzel',serif;font-size:50px}
.cta-last .rule{background:var(--white);width:80px;height:3px}
.cta-text{left:170px;top:3716px;width:860px;text-align:center;color:var(--white);font-size:14px;line-height:28px}
.btn-cta{left:416px;top:3820px;width:368px;height:52px;background:var(--white);color:var(--navy);font-size:18px;font-weight:600}

/* footer */
.footer-bg{left:0;top:3966px;width:1200px;height:433px}
.foot-brand{left:70px;top:4240px;width:270px;text-align:center;color:var(--navy);font-family:'Cinzel',serif;line-height:1.1}
.foot-brand .l1{display:block;font-size:23px}
.foot-brand .l2{display:block;font-size:19px}
.foot-head{font-family:'Cinzel',serif;font-size:21px;color:var(--navy)}
.foot-head::after{content:"";display:block;width:36px;height:2px;background:var(--navy);margin-top:8px}
.quick-links{left:409px;top:4139px}
.quick-links ul{list-style:none;margin-top:22px}
.quick-links li{font-size:13px;color:#222;height:26px;display:flex;align-items:center;gap:10px}
.quick-links li::before{content:"";width:7px;height:7px;border-radius:50%;background:var(--navy)}
.contact{left:620px;top:4139px}
.contact-row{display:flex;gap:18px;margin-top:16px;font-size:13px;line-height:17px;color:#222}
.contact-row:first-of-type{margin-top:22px}
.c-icon{width:22px;height:22px;background:var(--navy);border-radius:3px;display:flex;align-items:center;justify-content:center;flex:none;margin-top:6px}
.newsletter{left:900px;top:4137px;width:200px}
.newsletter p{font-size:13px;line-height:17px;color:#222;margin-top:22px}
.nl-input{width:196px;height:32px;border:1px solid #ddd;margin-top:18px;background:#fff}
.nl-btn{width:99px;height:29px;background:var(--navy);color:var(--white);font-size:9.5px;font-weight:600;display:flex;align-items:center;justify-content:center;margin-top:12px}
.bottom-bar{left:0;top:4399px;width:1200px;height:59px;background:var(--navy);color:var(--white);font-size:11px}
.bottom-bar .copy{left:59px;top:22px}
.social{top:17px;width:24px;height:24px;background:var(--white);border-radius:2px}
</style>
</head>
<body>

<!-- header -->
<div class="abs topbar">
  <div class="abs phone">
    <svg width="15" height="15" viewBox="0 0 24 24"><path d="M6.6 10.8a15 15 0 0 0 6.6 6.6l2.2-2.2a1 1 0 0 1 1-.25 11.4 11.4 0 0 0 3.6.57 1 1 0 0 1 1 1V20a1 1 0 0 1-1 1A17 17 0 0 1 3 4a1 1 0 0 1 1-1h3.5a1 1 0 0 1 1 1c0 1.25.2 2.45.57 3.57a1 1 0 0 1-.25 1z" fill="#fff"/></svg>
    <span>8012 345 6789</span>
  </div>
  <div class="abs mail">
    <span>info@websitename.com</span>
    <svg width="18" height="14" viewBox="0 0 18 14"><rect x="0" y="0" width="18" height="14" rx="1" fill="#fff"/><path d="M1 1l8 7 8-7" stroke="#0c0b4f" stroke-width="1.5" fill="none"/></svg>
  </div>
</div>
<div class="abs navbar"></div>
<span class="abs nav-link active" style="left:97px">HOME</span>
<span class="abs nav-link" style="left:190px">ABOUT US</span>
<span class="abs nav-link" style="left:314px">OUR MISSION</span>
<span class="abs nav-link" style="left:815px">SERVICES</span>
<span class="abs nav-link" style="left:903px">OUR TEAM</span>
<span class="abs nav-link" style="left:997px">CONTACT US</span>
<svg class="abs logo-plate" viewBox="0 0 1200 160">
  <defs><filter id="plateShadow" x="-10%" y="-10%" width="120%" height="130%"><feDropShadow dx="0" dy="2" stdDeviation="3" flood-opacity=".15"/></filter></defs>
  <polygon points="580,0 636,0 771,95 727,152 489,152 445,95" fill="#fff" filter="url(#plateShadow)"/>
</svg>
<div class="abs brand-dot"></div>
<div class="abs brand"><span class="l1">Alderpeak Wealth</span><span class="l2">Management</span></div>

<!-- hero -->
<div class="abs hero-photo" role="img" aria-label="Photo of two hikers with backpacks climbing a grassy slope before snowy mountains"></div>
<svg class="abs hero-edge" viewBox="0 640 1200 200">
  <polygon points="0,665 599,800 1200,655 1200,668 599,824 0,680" fill="#9a9a9a"/>
</svg>
<div class="abs hero-kicker">WELCOME TO</div>
<div class="abs hero-title">ALDERPEAK WEALTH<br>MANAGEMENT</div>
<div class="abs btn btn-hero">LEARN MORE
  <svg width="20" height="20" viewBox="0 0 20 20"><circle cx="10" cy="10" r="10" fill="#fff"/><path d="M8 5.5l4.5 4.5L8 14.5" stroke="#0c0b4f" stroke-width="2.4" fill="none"/></svg>
</div>
<div class="abs scroll-cue">
  <svg width="14" height="18" viewBox="0 0 14 18"><path d="M7 1v15M2 11l5 5 5-5" stroke="#555" stroke-width="1.6" fill="none"/></svg>
</div>

<!-- about -->
<div class="abs about-photo" role="img" aria-label="Portrait photo of a smiling senior financial advisor in a dark suit and glasses"></div>
<div class="abs about-title">ABOUT US</div>
<div class="abs about-sub">WHO WE ARE <span class="rule" style="width:110px"></span></div>
<p class="abs about-text">Lorem ipsum dolor sit amet, consectetur adipiscing elit. Sed pharetra, turpis vitae tincidunt tempus, ipsum magna varius mauris, et dictum nulla neque ac turpis. Etiam finibus est metus, eu viverra velit auctor ac. Nam luctus lorem felis, quis vulputate quam convallis elementum. Maecenas malesuada risus vitae tristique imperdiet. Interdum et malesuada fames ac ante ipsum primis in faucibus. Cras tristique nunc a tellus semper, et ultrices mauris vulputate.</p>
<div class="abs btn btn-small">READ MORE
  <svg width="17" height="17" viewBox="0 0 20 20"><circle cx="10" cy="10" r="10" fill="#fff"/><path d="M8 5.5l4.5 4.5L8 14.5" stroke="#0c0b4f" stroke-width="2.4" fill="none"/></svg>
</div>

<!-- why choose us -->
<svg class="abs why-bg" viewBox="0 1411 1200 861">
  <polygon points="0,1602 599,1411 1200,1602 1200,2272 0,2272" fill="#f6f6f6"/>
</svg>
<div class="abs why-kicker"><span class="rule" style="width:80px;height:3px"></span>WHY CHOOSE US<span class="rule" style="width:80px;height:3px"></span></div>
<div class="abs why-title">EXPERT ADVICE FOR<br>EVERY LIFE STAGE</div>
<div class="abs emblem-mark" aria-hidden="true"></div>
<div class="abs emblem-name">Alderpeak Wealth<br>Management</div>

<div class="abs feat-diamond navy" style="left:419px;top:1792px"></div>
<div class="abs feat-diamond navy" style="left:708px;top:1792px"></div>
<div class="abs feat-diamond light" style="left:323px;top:1936px"></div>
<div class="abs feat-diamond light" style="left:800px;top:1936px"></div>
<div class="abs feat-diamond navy" style="left:219px;top:2078px"></div>
<div class="abs feat-diamond navy" style="left:905px;top:2078px"></div>

<!-- feature icons -->
<svg class="abs feat-icon" style="left:438px;top:1811px" viewBox="0 0 60 60" fill="none" stroke="#fff" stroke-width="2.4"><circle cx="34" cy="24" r="11"/><circle cx="34" cy="24" r="5"/><circle cx="20" cy="34" r="5"/><path d="M10 50c0-7 4-11 10-11s10 4 10 11"/></svg>
<svg class="abs feat-icon" style="left:727px;top:1811px" viewBox="0 0 60 60" fill="none" stroke="#fff" stroke-width="2.4"><circle cx="30" cy="20" r="5"/><circle cx="16" cy="24" r="4"/><circle cx="44" cy="24" r="4"/><path d="M22 38c0-6 3-9 8-9s8 3 8 9M9 38c0-5 3-7 7-7M51 38c0-5-3-7-7-7M14 44c6 7 26 7 32 0"/></svg>
<svg class="abs feat-icon" style="left:342px;top:1955px" viewBox="0 0 60 60" fill="none" stroke="#fff" stroke-width="2.4"><circle cx="30" cy="18" r="5"/><path d="M22 32c0-5 3-8 8-8s8 3 8 8M10 44h12l8 4 14-6M10 44v-6h8l8 3"/><path d="M42 16v10M47 14v12M52 18v8"/></svg>
<svg class="abs feat-icon" style="left:819px;top:1955px" viewBox="0 0 60 60" fill="none" stroke="#fff" stroke-width="2.4"><path d="M18 50V40c-5-3-8-8-8-14 0-10 8-17 18-17s18 7 18 17c0 4-1 6-3 8v6h-6v10"/><circle cx="28" cy="26" r="8"/><circle cx="28" cy="26" r="2"/></svg>
<svg class="abs feat-icon" style="left:238px;top:2097px" viewBox="0 0 60 60" fill="none" stroke="#fff" stroke-width="2.4"><rect x="8" y="20" width="32" height="22" rx="4"/><path d="M16 42v7l7-7"/><path d="M26 20v-6h26v18h-12"/><circle cx="16" cy="31" r="2" fill="#fff"/><circle cx="24" cy="31" r="2" fill="#fff"/><circle cx="32" cy="31" r="2" fill="#fff"/></svg>
<svg class="abs feat-icon" style="left:924px;top:2097px" viewBox="0 0 60 60" fill="none" stroke="#fff" stroke-width="2.6"><path d="M10 20h10l18 20h10M10 40h10l18-20h10M44 15l5 5-5 5M44 35l5 5-5 5"/></svg>

<div class="abs feat right" style="left:136px;top:1784px;width:250px">
  <div class="feat-title">Expert Advisors</div>
  <div class="feat-text">Lorem ipsum dolor sit amet, cons<br>ect etur adipiscing elit. Sed</div>
</div>
<div class="abs feat" style="left:838px;top:1784px;width:250px">
  <div class="feat-title">Comprehensive<br>Services</div>
  <div class="feat-text">Lorem ipsum dolor sit amet, cons<br>ect etur adipiscing elit. Sed</div>
</div>
<div class="abs feat right" style="left:60px;top:1939px;width:240px">
  <div class="feat-title">Personalized<br>Approach</div>
  <div class="feat-text">Lorem ipsum dolor sit amet,<br>ect etur adipiscing elit.</div>
</div>
<div class="abs feat" style="left:932px;top:1933px;width:250px">
  <div class="feat-title">Client-Centric<br>Philosophy</div>
  <div class="feat-text">Lorem ipsum dolor sit amet,<br>cons ect etur adipiscing elit.</div>
</div>
<div class="abs feat right" style="left:16px;top:2090px;width:180px">
  <div class="feat-title">Transparent<br>Communication</div>
  <div class="feat-text">Lorem ipsum dolor<br>sit amet</div>
</div>
<div class="abs feat" style="left:1027px;top:2088px;width:150px">
  <div class="feat-title">Flexibility</div>
  <div class="feat-text">Lorem ipsum<br>dolor sit amet,<br>cons ect etur</div>
</div>

<!-- services -->
<div class="abs services"></div>
<div class="abs svc-title">OUR SERVICES</div>
<div class="abs svc-sub"><span class="rule" style="width:100px"></span>WHAT WE DO<span class="rule" style="width:100px"></span></div>
<p class="abs svc-intro">Lorem ipsum dolor sit amet, consectetur adipiscing elit. Sed pharetra, turpis vitae tincidunt tempus, ipsum magna varius mauris,<br>et dictum nulla neque ac turpis. Etiam finibus est metus, eu viverra velit auctor ac.</p>

<div class="abs svc-diamond" style="left:311px;top:2865px"></div>
<div class="abs svc-diamond" style="left:659px;top:2865px"></div>
<div class="abs svc-diamond" style="left:128px;top:2682px"></div>
<div class="abs svc-diamond" style="left:841px;top:2682px"></div>
<div class="abs svc-diamond featured" style="left:484px;top:2672px"></div>

<div class="abs svc-icon" style="left:214px;top:2719px"><svg width="34" height="34" viewBox="0 0 34 34" fill="none" stroke="#fff" stroke-width="2"><rect x="7" y="4" width="20" height="26" rx="2"/><path d="M12 24v-4M17 24v-8M22 24v-11M11 10h8"/></svg></div>
<div class="abs svc-label" style="left:118px;top:2815px">Financial Planning</div>

<div class="abs svc-icon invert" style="left:570px;top:2709px"><svg width="34" height="34" viewBox="0 0 34 34" fill="none" stroke="#0c0b4f" stroke-width="2"><rect x="6" y="5" width="12" height="8" rx="1"/><rect x="17" y="9" width="12" height="8" rx="1"/><path d="M4 26l6-6h6l6 4 6-4M10 26l4 3 4-3"/></svg></div>
<div class="abs svc-label light" style="left:474px;top:2805px">Business Planning</div>
<div class="abs pill-read">READ MORE</div>

<div class="abs svc-icon" style="left:927px;top:2719px"><svg width="34" height="34" viewBox="0 0 34 34" fill="none" stroke="#fff" stroke-width="2"><circle cx="17" cy="17" r="11"/><path d="M17 9l7 13H10z"/><path d="M17 14v4"/></svg></div>
<div class="abs svc-label" style="left:831px;top:2815px">Risk Management</div>

<div class="abs svc-icon" style="left:397px;top:2903px"><svg width="34" height="34" viewBox="0 0 34 34" fill="none" stroke="#fff" stroke-width="2"><rect x="8" y="6" width="18" height="14" rx="1"/><path d="M12 16l4-4 3 3 4-5"/><path d="M5 28h8l6 2 10-5M5 28v-5h6l5 2"/></svg></div>
<div class="abs svc-label" style="left:301px;top:2999px">Investment Advising</div>

<div class="abs svc-icon" style="left:745px;top:2903px"><svg width="34" height="34" viewBox="0 0 34 34" fill="none" stroke="#fff" stroke-width="2"><circle cx="12" cy="14" r="5"/><path d="M12 11v6"/><rect x="20" y="8" width="8" height="18" rx="1"/><path d="M5 28h24"/><path d="M8 24h8"/></svg></div>
<div class="abs svc-label" style="left:649px;top:2999px">Retirement Planning</div>

<div class="abs btn btn-view">VIEW MORE
  <svg width="17" height="17" viewBox="0 0 20 20"><circle cx="10" cy="10" r="10" fill="#fff"/><path d="M8 5.5l4.5 4.5L8 14.5" stroke="#0c0b4f" stroke-width="2.4" fill="none"/></svg>
</div>

<!-- call to action -->
<div class="abs cta"></div>
<div class="abs cta-kicker">ARE YOU READY</div>
<div class="abs cta-title">TO BEGIN THE JOURNEY TO YOUR<br>FINANCIAL SUMMIT?</div>
<div class="abs cta-last"><span class="rule"></span>LET'S START TODAY!<span class="rule"></span></div>
<p class="abs cta-text">Let us help you take the first step towards the financial freedom and long - term security. Our &nbsp;Dedicated &nbsp;team of<br>experts is here to guide you through personalized stratergies testicated to your goal</p>
<div class="abs btn btn-cta">SCHEDULE A CONSULTATION
  <svg width="20" height="20" viewBox="0 0 20 20"><circle cx="10" cy="10" r="10" fill="#0c0b4f"/><path d="M8 5.5l4.5 4.5L8 14.5" stroke="#fff" stroke-width="2.4" fill="none"/></svg>
</div>

<!-- footer -->
<svg class="abs footer-bg" viewBox="0 3966 1200 433">
  <polygon points="0,4139 599,3966 1200,4139 1200,4399 0,4399" fill="#fff"/>
</svg>
<div class="abs foot-brand"><span class="l1">Alderpeak Wealth</span><span class="l2">Management</span></div>

<div class="abs quick-links">
  <div class="foot-head">QUICK LINKS</div>
  <ul>
    <li>About Us</li><li>Who We Are</li><li>Our Mission</li><li>Services</li><li>Our Team</li><li>Contact Us</li>
  </ul>
</div>

<div class="abs contact">
  <div class="foot-head">CONTACT US</div>
  <div class="contact-row">
    <span class="c-icon"><svg width="11" height="11" viewBox="0 0 24 24"><path d="M6.6 10.8a15 15 0 0 0 6.6 6.6l2.2-2.2a1 1 0 0 1 1-.25 11.4 11.4 0 0 0 3.6.57 1 1 0 0 1 1 1V20a1 1 0 0 1-1 1A17 17 0 0 1 3 4a1 1 0 0 1 1-1h3.5a1 1 0 0 1 1 1c0 1.25.2 2.45.57 3.57a1 1 0 0 1-.25 1z" fill="#fff"/></svg></span>
    <div>CALL US<br>8012 345 6789</div>
  </div>
  <div class="contact-row">
    <span class="c-icon"><svg width="12" height="9" viewBox="0 0 18 14"><rect width="18" height="14" fill="#fff"/><path d="M1 1l8 7 8-7" stroke="#0c0b4f" stroke-width="1.6" fill="none"/></svg></span>
    <div>EMAIL US<br>info@websitename.com</div>
  </div>
  <div class="contact-row">
    <span class="c-icon"><svg width="10" height="13" viewBox="0 0 10 14"><path d="M5 0a5 5 0 0 1 5 5c0 4-5 9-5 9S0 9 0 5a5 5 0 0 1 5-5z" fill="#fff"/><circle cx="5" cy="5" r="1.8" fill="#0c0b4f"/></svg></span>
    <div>Address Line Dummy here<br>Address line dummy</div>
  </div>
</div>

<div class="abs newsletter">
  <div class="foot-head">OUR NEWSLETTER</div>
  <p>Subscribe our newsletter to get the latest news.</p>
  <div class="nl-input"></div>
  <div class="nl-btn">SUBSCRIBE</div>
</div>

<div class="abs bottom-bar">
  <span class="abs copy">Copyright © 2024 All Rights Reserved By Company name</span>
  <span class="abs social" style="left:1006px" aria-label="Social profile"></span>
  <span class="abs social" style="left:1039px" aria-label="Social profile"></span>
  <span class="abs social" style="left:1071px" aria-label="Social profile"></span>
  <span class="abs social" style="left:1103px" aria-label="Social profile"></span>
</div>

</body>
</html>
```